Crestline Finance Needs a punchy 6 page Flyer

We need a flyer that we can hand to potential referral sources and clients that details what we do, is punchy and to the point. This will be one of our primary introduction marketing tools.
We are a Mortgage Broking Business ie we arrange finance for clients. We are also affiliated with a Financial Planning Practice.
We would like to see designs that integrate the tow business's. We would like to see our Current corporate Blue colours (RGS) be represented with Green also. The final design should represent financial safety, integrity and growth. As a guide the attached brochures are provided, we would like to see a "notes" page incorporated, we prefer the "Crestline Finance" structure and design. The wording will be provided however design, formatting and graphics will be required.

Target Market(s)

Professional referral sources and clients being business's & individuals

Industry/Entity Type

Financial

Colors

Requirements
Must have
• Look sharp, simple English, good flow and integration
Nice to have
• Cooler colours

```html
<!DOCTYPE html>
<html lang="en">
<head>
<meta charset="utf-8">
<title>Crestline Finance – General / Business Insurance</title>
<link href="https://fonts.googleapis.com/css2?family=Josefin+Sans:wght@300;400;600;700&display=swap" rel="stylesheet">
<style>
  :root {
    --blue: #1f5fb4;
    --blue-dark: #0f3e86;
    --ink: #2b2b2b;
    --paper: #ffffff;
    --note-top: #fff6a8;
    --note-bottom: #f3e270;
    --calc-dark: #3a3f47;
    --calc-warm: #b88a4a;
  }
  html, body { margin: 0; padding: 0; overflow: hidden; background: var(--paper); }
  .page {
    position: relative; width: 849px; height: 1200px; overflow: hidden;
    background: var(--paper);
    font-family: "Josefin Sans", "Century Gothic", sans-serif;
    color: var(--ink);
  }
  .corner { position: absolute; }
  .corner--top { top: 0; right: 0; }
  .corner--bottom { bottom: 0; left: 0; }

  .section-title {
    position: absolute; left: 40px; margin: 0;
    font-weight: 400; font-size: 36px; line-height: 42px; color: var(--blue);
  }
  .section-rule { position: absolute; left: 0; height: 4px; background: var(--blue); }

  .copy {
    position: absolute; margin: 0;
    font-size: 13px; line-height: 16px; font-weight: 400;
  }
  .copy--justified { text-align: justify; }
  .lead-in {
    position: absolute; margin: 0; left: 40px;
    font-size: 15px; font-weight: 700; color: var(--blue-dark);
  }
  .bullets {
    position: absolute; margin: 0; padding: 0; list-style: none;
    display: grid; grid-auto-flow: column;
    font-size: 13px; line-height: 20px;
  }
  .bullets li { position: relative; padding-left: 22px; white-space: nowrap; }
  .bullets li::before {
    content: ""; position: absolute; left: 3px; top: 5px;
    width: 7px; height: 7px; background: var(--blue); transform: rotate(45deg);
  }
  .bullets--insurance { top: 232px; left: 58px; grid-template-rows: repeat(2, 20px); grid-template-columns: 200px 200px; }
  .bullets--partners { top: 742px; left: 99px; grid-template-rows: repeat(3, 20px); grid-template-columns: 222px 210px; }

  .photo-calculator {
    position: absolute; left: 436px; top: 336px; width: 413px; height: 226px;
    background: radial-gradient(ellipse at 35% 45%, #6b7179 0%, var(--calc-dark) 55%, var(--calc-warm) 100%);
  }
  .sticky-note {
    position: absolute; left: 552px; top: 748px; width: 262px; height: 300px;
    background: linear-gradient(170deg, var(--note-top), var(--note-bottom));
    box-shadow: 4px 6px 10px rgba(0,0,0,0.18);
  }
</style>
</head>
<body>
<main class="page">
  <svg class="corner corner--top" width="130" height="128" viewBox="0 0 130 128" aria-hidden="true">
    <polygon points="0,0 130,0 130,128" fill="var(--blue-dark)"/>
    <polygon points="40,0 130,0 130,88" fill="var(--blue)"/>
  </svg>

  <h1 class="section-title" style="top:14px;">General / Business Insurance</h1>
  <div class="section-rule" style="top:60px; width:668px;"></div>

  <p class="copy" style="top:88px; left:40px; width:740px;">
    Everybody needs insurance, but few of us know if we have ‘enough’. At Crestline Finance we can arrange for our business partners at Ardent Cover to call you and go through your general insurance needs. If the insurance is related to a new property purchase we can even advise them of the amount the valuer has specified the property should be insured for.
  </p>

  <p class="lead-in" style="top:206px;">Ardent Cover can assist you with:</p>
  <ul class="bullets bullets--insurance">
    <li>Building insurance</li>
    <li>Contents insurance</li>
    <li>Landlord insurance</li>
    <li>Car insurance</li>
  </ul>

  <p class="copy copy--justified" style="top:288px; left:40px; width:376px;">
    We also don’t believe anyone should have debt without the appropriate personal insurances, but life insurance and income protection can be expensive. Dan can help you put your insurances in the right environment to lessen their impact on your budget, without jeopardising your cover.
  </p>
  <p class="copy copy--justified" style="top:376px; left:40px; width:376px;">
    If you run a business you’ll know that insurance is both essential, and potentially expensive. At Crestline Finance we can make sure that your business insurance is appropriate to your needs, so you’re neither under insured nor over insured.
  </p>
  <p class="copy" style="top:462px; left:40px; width:376px;">
    It may be that income protection is the right option for you, but business continuance insurance may be the better option. Issues like this need to be discussed with Dan so you get what you need and not what someone else wanted to sell you!
  </p>

  <div class="photo-calculator" role="img" aria-label="Photo of a calculator beside a pile of coins and banknotes"></div>

  <h2 class="section-title" style="top:602px;">Referral Partnerships</h2>
  <div class="section-rule" style="top:648px; width:708px;"></div>

  <p class="copy" style="top:676px; left:57px; width:700px;">
    If we uncover other services that you require assistance with our extensive contact base will allow us to refer you to people we know and trust:
  </p>
  <ul class="bullets bullets--partners">
    <li>Solicitors</li>
    <li>Conveyancers</li>
    <li>Real estate agents</li>
    <li>Property managers</li>
    <li>Investment property specialists</li>
    <li>Accountants</li>
  </ul>

  <p class="copy copy--justified" style="top:862px; left:141px; width:320px;">
    Ensuring that everyone is moving in the same direction means you have a better experience, and get a better result.
  </p>

  <div class="sticky-note" role="img" aria-label="Yellow sticky note pinned to the page for notes"></div>

  <svg class="corner corner--bottom" width="272" height="350" viewBox="0 0 272 350" aria-hidden="true">
    <polygon points="0,0 272,350 0,350" fill="var(--blue)"/>
    <polygon points="0,110 190,350 0,350" fill="var(--blue-dark)"/>
  </svg>
</main>
</body>
</html>
```